Generic Label Design for Kids Craft Kits

I'm starting a new online / retail business that will package different craft materials and instructions into craft projects for kids from ages 2-12. I need a label for the front of the packages that looks professional. Although I'm interested in a very professional design (the kits will not be sold at a low cost) I'm also aiming for a 'natural' / crafty look to my packaging. The packaging will be hand-made with Kraft boxes / bags as the basic material. I will be adding hand-made embellishments to make the packaging look attractive (ex: a paper or crochet flower will be used to seal the packaging and hand-made twine ropes will be used as the handle). On the back of the package, I will be using a custom-made rubber stamp to imprint my Logo and Website address. I've included some pictures of packaging material that I really liked
Updates

       Please see updated brief and new deadline, this should make the project much clearer and easier.

Target Market(s)

End user = kids but buyer = parents

Industry/Entity Type

Business

Requirements
Must have

• The label design should include:
- A place for my logo at the top (it is a simple logo with the text: The Maple Makery in Google Fonts type Dancing Script. There is a small flower as the dot of the i in Makery)
- You can use these colors: #eaeac5, #e5b7b7, #669899, #947057, #8cc1ba, #fbfaf3 or any other similar / complementary colors
- a placeholder for me to add in (through photoshop) a digital image of the actual craft that is included in the package
- a place where I can put a small description of the activity or point out some cool features of the project
- a place where I can indicate the age suitability of the product
- a place where I can detail a short description of the activity,what is included in the kit

Other requirements:
- my online store is similar to this one in design so you can visit this for inspiration on look and feel: http://bramble-muffin-hollow.shopwren.example/
- the files that you provide should allow me to resize the label if I need to change the dimensions of my packaging (vector preferred)
- the look and feel should be attractive for children but still professional and sticking to the look and feel for my online store

```html
<!DOCTYPE html>
<html lang="en">
<head>
<meta charset="utf-8">
<title>The Maple Makery – Craft Kit Label</title>
<link rel="stylesheet" href="https://fonts.googleapis.com/css2?family=Source+Sans+3:wght@300;400&display=swap">
<style>
  :root {
    --paper: #ffffff;
    --mint: #8ecfbc;
    --rose: #ce8787;
    --butter: #e5e3aa;
    --bark: #947057;
    --ink-light: #ffffff;
  }
  html, body {
    margin: 0;
    padding: 0;
    overflow: hidden;
    background: var(--paper);
  }
  .label {
    position: relative;
    width: 1200px;
    height: 1000px;
    background: var(--paper);
    overflow: hidden;
  }
  .label__art {
    position: absolute;
    top: 0;
    left: 0;
    display: block;
  }
  .heart-band {
    position: absolute;
    left: 0;
    width: 1200px;
    height: 46px;
    background: linear-gradient(90deg, var(--mint), var(--rose), var(--mint), var(--rose), var(--mint), var(--rose));
    opacity: 0.5;
  }
  .heart-band--top { top: 110px; }
  .heart-band--bottom { top: 766px; }
  .brand-name,
  .product-description,
  .circle-text {
    font-family: "Source Sans 3", "Myriad Pro", Arial, sans-serif;
  }
  .brand-name { font-weight: 300; fill: var(--mint); }
  .product-description { font-weight: 400; fill: var(--rose); }
  .circle-text { font-weight: 400; fill: var(--ink-light); }
</style>
</head>
<body>
<main class="label">
  <div class="heart-band heart-band--top" role="img" aria-label="Row of alternating mint and rose hearts"></div>

  <svg class="label__art" width="1200" height="1000" viewBox="0 0 1200 1000">
    <g class="brand">
      <text class="brand-name" x="190" y="268" font-size="84" textLength="830" lengthAdjust="spacing">The Maple Makery</text>
      <circle class="brand-dot" cx="1040" cy="222" r="7" fill="var(--bark)"/>
    </g>

    <text class="product-description" x="575" y="333" font-size="48" textLength="473" lengthAdjust="spacingAndGlyphs">description of product</text>

    <g class="age-badge">
      <circle cx="263" cy="577" r="121" fill="var(--butter)"/>
      <text class="circle-text" x="157" y="579" font-size="16" textLength="204" lengthAdjust="spacingAndGlyphs">indication of age suitability</text>
    </g>

    <g class="craft-photo">
      <circle cx="585" cy="577" r="128" fill="var(--rose)"/>
      <text class="circle-text" x="505" y="561" font-size="25" textLength="73" lengthAdjust="spacingAndGlyphs">photo</text>
      <text class="circle-text" x="505" y="595" font-size="25" textLength="163" lengthAdjust="spacingAndGlyphs">of actual craft</text>
    </g>

    <g class="kit-contents">
      <circle cx="906" cy="581" r="124" fill="var(--mint)"/>
      <text class="circle-text" x="805" y="553" font-size="24" textLength="201" lengthAdjust="spacingAndGlyphs">what is included:</text>
      <circle cx="821" cy="577" r="3.5" fill="var(--ink-light)"/>
      <circle cx="821" cy="609" r="3.5" fill="var(--ink-light)"/>
      <circle cx="821" cy="642" r="3.5" fill="var(--ink-light)"/>
    </g>
  </svg>

  <div class="heart-band heart-band--bottom" role="img" aria-label="Row of alternating mint and rose hearts"></div>
</main>
</body>
</html>
```